1 Page for Computer Repair Website

Looking for a 1 page website with a design that compliments the business card and pamphlet that have already been made (attached files). It should look business professional and easy to read. Email and phone number should be somewhere near the top of the website, visible when the page loads. I don't want any forms for people to mess with. No "Contact Us" form or entering in email for newsletter. Customers will just be looking at this site to confirm we are professionals and have our business in order.

Target Market(s)

Home and small business

Industry/Entity Type

Computer Repair

Coding

Coded - Design and coding required

Number of Pages Required

1 page

Font styles to use
Other font styles liked:
• Helvetica variations used in pamphlet and card

Colors
0455a3
cfdeed
85abd2
3276b5
85cae6
ffffff

Requirements
Must have
• Compliment the pamphlet and business card in color choices and font use. Pleasing to the eye and easy to read through categories and text.
Should not have
• Forms. No "enter name and email here" or anything of the sort.

```html
<!DOCTYPE html>
<html lang="en">
<head>
<meta charset="utf-8">
<title>Pulse Tech Computer Services</title>
<link href="https://fonts.googleapis.com/css2?family=Arimo:wght@400;700&display=swap" rel="stylesheet">
<style>
  :root {
    --brand-blue: #0455a3;
    --mid-blue: #3276b5;
    --soft-blue: #85abd2;
    --sky-blue: #85cae6;
    --pale-blue: #cfdeed;
    --white: #ffffff;
    --nav-grey: #3f4247;
    --band-grey: #e4e6e9;
    --footer-dark: #2f3236;
    --navy: #0b2a57;
    --text-dark: #2b2b2b;
    --text-muted: #555a60;
  }
  * { box-sizing: border-box; margin: 0; padding: 0; }
  html, body { width: 816px; height: 1200px; overflow: hidden; }
  body { font-family: "Arimo", "Helvetica Neue", Arial, sans-serif; color: var(--text-dark); background: var(--white); position: relative; }

  /* Header */
  .site-header { position: absolute; top: 0; left: 0; width: 816px; height: 50px; background: var(--white); }
  .brand { position: absolute; left: 24px; top: 9px; display: flex; align-items: center; gap: 8px; }
  .brand-mark { width: 14px; height: 14px; background: var(--brand-blue); }
  .brand-name { font-size: 26px; font-weight: 700; color: var(--brand-blue); letter-spacing: 0.5px; line-height: 1; }
  .search-box { position: absolute; right: 96px; top: 9px; width: 170px; height: 20px; border: 1px solid #c9ccd1; font-size: 10px; color: #8a8f96; padding: 4px 6px; }
  .search-btn { position: absolute; right: 78px; top: 9px; width: 20px; height: 20px; background: var(--brand-blue); }
  .contact-line { position: absolute; right: 96px; top: 34px; display: flex; gap: 12px; font-size: 9.5px; color: var(--brand-blue); }
  .contact-line span { display: flex; align-items: center; gap: 4px; }

  /* Navigation */
  .main-nav { position: absolute; top: 50px; left: 0; width: 816px; height: 30px; background: var(--nav-grey); display: flex; padding-left: 24px; }
  .main-nav a { color: var(--white); font-size: 11px; text-decoration: none; line-height: 30px; padding: 0 11px; border-right: 1px solid #5b5f65; }
  .main-nav a:first-child { background: #2a2c30; }

  /* Hero */
  .hero { position: absolute; top: 80px; left: 0; width: 816px; height: 322px; }
  .hero-photo { width: 100%; height: 100%; background: linear-gradient(100deg, #3f4a52 0%, #8b939a 28%, #c9c7c0 48%, #6f7a72 70%, #3b4640 100%); }
  .hero-tag { position: absolute; left: 490px; width: 205px; font-size: 10px; padding: 7px 10px; }
  .hero-tag.light { top: 128px; background: var(--white); color: var(--text-dark); }
  .hero-tag.blue { top: 156px; background: var(--brand-blue); color: var(--white); }

  /* Services strip */
  .services-strip { position: absolute; top: 402px; left: 0; width: 816px; height: 143px; background: var(--band-grey); }
  .service-tile { position: absolute; top: 8px; width: 190px; height: 114px; }
  .service-tile .tile-photo { width: 100%; height: 100%; }
  .service-tile .tile-label { position: absolute; left: 0; right: 0; top: 36px; text-align: center; color: var(--white); font-size: 11px; font-weight: 700; background: rgba(0,0,0,0.35); padding: 4px 0; }
  .service-tile .tile-icon { position: absolute; right: 0; bottom: 0; width: 18px; height: 18px; background: var(--mid-blue); display: flex; align-items: center; justify-content: center; }

  /* Welcome */
  .welcome { position: absolute; top: 545px; left: 0; width: 816px; height: 195px; }
  .welcome-photo { position: absolute; inset: 0; background: linear-gradient(90deg, #1c1f22 0%, #3a3f44 35%, #2c3034 65%, #4a4d50 100%); }
  .welcome-body { position: absolute; inset: 0; text-align: center; color: var(--white); padding: 20px 110px 0; }
  .welcome-title { font-size: 21px; font-weight: 700; margin-bottom: 10px; }
  .welcome-text { font-size: 10.5px; line-height: 1.5; color: #e9ebee; }
  .btn-primary { display: inline-block; margin-top: 14px; background: var(--brand-blue); color: var(--white); font-size: 11px; padding: 8px 18px; text-decoration: none; }

  /* Feature cards */
  .features { position: absolute; top: 740px; left: 0; width: 816px; height: 252px; background: var(--band-grey); }
  .feature-card { position: absolute; top: 20px; width: 176px; height: 214px; background: var(--white); text-align: center; }
  .feature-card .card-photo { height: 108px; }
  .feature-card h3 { font-size: 11px; font-weight: 700; margin: 12px 0 4px; }
  .feature-card p { font-size: 9px; line-height: 1.4; color: var(--text-muted); padding: 0 12px; }
  .btn-dark { display: inline-block; margin-top: 9px; background: var(--footer-dark); color: var(--white); font-size: 9px; padding: 6px 12px; text-decoration: none; }

  /* Footer */
  .site-footer { position: absolute; top: 992px; left: 0; width: 816px; height: 174px; background: var(--footer-dark); color: #d7d9dc; }
  .footer-col { position: absolute; top: 22px; width: 170px; }
  .footer-col h4 { font-size: 13px; font-weight: 400; color: var(--white); padding-bottom: 8px; border-bottom: 1px solid #5a5e63; margin-bottom: 10px; }
  .footer-col li { list-style: none; font-size: 9.5px; line-height: 1.75; }
  .copyright { position: absolute; top: 1166px; left: 0; width: 816px; height: 34px; background: var(--navy); color: #cfdeed; font-size: 9px; text-align: center; line-height: 34px; }
</style>
</head>
<body>

<header class="site-header">
  <div class="brand"><span class="brand-mark"></span><span class="brand-name">Pulse Tech</span></div>
  <div class="search-box">Search here</div>
  <div class="search-btn"></div>
  <div class="contact-line">
    <span>
      <svg width="11" height="8" viewBox="0 0 11 8"><rect x="0.5" y="0.5" width="10" height="7" fill="none" stroke="#0455a3"/><path d="M0.5 0.5 L5.5 4.5 L10.5 0.5" fill="none" stroke="#0455a3"/></svg>
      hello@pulsetechrepair.com
    </span>
    <span>
      <svg width="9" height="10" viewBox="0 0 9 10"><path d="M2 0.5 L3.5 3 L2.5 4 Q3.5 6.5 5.5 7.5 L6.5 6.5 L8.5 8 L7 9.5 Q1 8 0.5 1.5 Z" fill="#0455a3"/></svg>
      555-014-2290
    </span>
  </div>
</header>

<nav class="main-nav">
  <a href="#">Home</a><a href="#">About Us</a><a href="#">Services</a><a href="#">Pricing</a><a href="#">Contact Us</a>
</nav>

<section class="hero">
  <div class="hero-photo" role="img" aria-label="Photo of a technician working on a laptop in a bright office"></div>
  <div class="hero-tag light">Lorem ipsum dolor amet sit</div>
  <div class="hero-tag blue">Lorem ipsum dolor sit amet consect amet</div>
</section>

<section class="services-strip">
  <div class="service-tile" style="left:110px">
    <div class="tile-photo" role="img" aria-label="Photo of computer hardware being repaired" style="background:linear-gradient(135deg,#6d6a66,#a8a29a 60%,#4f4c48)"></div>
    <div class="tile-label">Lorem Ipsum Hardware Repair</div>
    <div class="tile-icon"><svg width="10" height="10" viewBox="0 0 10 10"><circle cx="4" cy="4" r="3" fill="none" stroke="#fff" stroke-width="1.4"/><path d="M6.2 6.2 L9 9" stroke="#fff" stroke-width="1.6"/></svg></div>
  </div>
  <div class="service-tile" style="left:313px">
    <div class="tile-photo" role="img" aria-label="Photo of a laptop screen showing a software update" style="background:linear-gradient(135deg,#8d8f92,#c7c9cb 55%,#6a6d70)"></div>
    <div class="tile-label">Lorem Software Upgrades</div>
    <div class="tile-icon"><svg width="10" height="10" viewBox="0 0 10 10"><circle cx="4" cy="4" r="3" fill="none" stroke="#fff" stroke-width="1.4"/><path d="M6.2 6.2 L9 9" stroke="#fff" stroke-width="1.6"/></svg></div>
  </div>
  <div class="service-tile" style="left:517px">
    <div class="tile-photo" role="img" aria-label="Photo of a desk with a computer being installed" style="background:linear-gradient(135deg,#7f8f9c,#b9c6cf 55%,#5e6c78)"></div>
    <div class="tile-label">Lorem Ipsum Installation</div>
    <div class="tile-icon"><svg width="10" height="10" viewBox="0 0 10 10"><circle cx="4" cy="4" r="3" fill="none" stroke="#fff" stroke-width="1.4"/><path d="M6.2 6.2 L9 9" stroke="#fff" stroke-width="1.6"/></svg></div>
  </div>
</section>

<section class="welcome">
  <div class="welcome-photo" role="img" aria-label="Dark photo of a keyboard and notebook on a desk"></div>
  <div class="welcome-body">
    <h2 class="welcome-title">Welcome to Pulse Tech Computer Services</h2>
    <p class="welcome-text">Lorem ipsum dolor sit amet, consectetuer adipiscing elit. Aenean commodo ligula eget dolor. Aenean massa. Cum sociis natoque penatibus et magnis dis parturient montes, nascetur ridiculus mus. Donec quam felis, ultricies nec, pellentesque eu, pretium quis, sem. Nulla consequat massa quis enim. Donec pede justo, fringilla vel, aliquet nec, vulputate eget, arcu. In enim justo, rhoncus ut, imperdiet a, venenatis vitae, justo. Nullam dictum felis eu pede mollis pretium. Integer tincidunt. Cras dapibus. Vivamus elementum semper nisi. Aenean vulputate eleifend tellus. Aenean leo ligula, porttitor eu, consequat vitae, eleifend ac, enim.</p>
    <a class="btn-primary" href="#">Read More</a>
  </div>
</section>

<section class="features">
  <article class="feature-card" style="left:110px">
    <div class="card-photo" role="img" aria-label="Illustration of a hand using a computer mouse" style="background:linear-gradient(180deg,#dfe8f1,#85abd2)"></div>
    <h3>Lorem Ipsum</h3>
    <p>Lorem ipsum dolor sit amet, consectetuer adipiscing elit. Aenean commodo ligula eget dolor.</p>
    <a class="btn-dark" href="#">Read More</a>
  </article>
  <article class="feature-card" style="left:320px">
    <div class="card-photo" role="img" aria-label="Illustration of a keyboard with a stethoscope" style="background:linear-gradient(180deg,#eef1f4,#9fb3c6)"></div>
    <h3>Lorem Ipsum</h3>
    <p>Lorem ipsum dolor sit amet, consectetuer adipiscing elit. Aenean commodo ligula eget dolor.</p>
    <a class="btn-dark" href="#">Read More</a>
  </article>
  <article class="feature-card" style="left:530px">
    <div class="card-photo" role="img" aria-label="Illustration of a repair tools badge" style="background:linear-gradient(180deg,#dbe9f4,#3276b5)"></div>
    <h3>Lorem Ipsum</h3>
    <p>Lorem ipsum dolor sit amet, consectetuer adipiscing elit. Aenean commodo ligula eget dolor.</p>
    <a class="btn-dark" href="#">Read More</a>
  </article>
</section>

<footer class="site-footer">
  <div class="footer-col" style="left:150px">
    <h4>Useful Links</h4>
    <ul><li>Home</li><li>About Us</li><li>Services</li><li>Pricing</li><li>Contact Us</li></ul>
  </div>
  <div class="footer-col" style="left:362px">
    <h4>Quick Links</h4>
    <ul><li>Lorem Ipsum</li><li>Lorem Ipsum</li><li>Lorem Ipsum</li><li>Lorem Ipsum</li><li>Lorem Ipsum</li></ul>
  </div>
  <div class="footer-col" style="left:545px">
    <h4>Address</h4>
    <ul><li>Lorem Ipsum</li><li>Suite 12, 48 Harbor Road</li><li>Lorem Ipsum Lorem</li><li>Springfield 500 000</li><li>Phone : 555-014-2290</li><li>E-mail : hello@pulsetechrepair.com</li></ul>
  </div>
</footer>
<div class="copyright">Copyright © Pulse Tech Computer Repair. All Rights Reserved</div>

</body>
</html>
```